Gestalten Sie ein tolles Selbstliebe-Buchcover
Design kam bei der Zielgruppe sehr gut an und war professionell umgesetzt. Die Kommunikation läuft zielgerichtet und nett und ich habe schnell alle Dateien bekommen, die ich brauche. Vielen Dank!
Hallo,
schön, dass Sie sich für diese Ausschreibung interessieren. Wir suchen ein Cover für unser Buch, das wir im Selbstverlag veröffentlichen werden.
Titel: Mondgarten am Nordufer
Untertitel 1: Wie du dich von negativen Gedanken befreist und eine liebevolle Beziehung zu dir selbst aufbaust
Untertitel Teil 2: 12 lebensverändernde Monate voller positiver Impulse und Liebe für dich
Das Buch soll (mehrheitlich) Frauen unterstützen, eine liebevolle Beziehung zu sich selbst aufzubauen, negative Gedanken loszulassen und innere Ruhe zu finden.
Aufgabenstellung
Wir sind für jegliche Vorschläge im Rahmen des Themas, der Samples und der Schieberegler offen.
Wichtig ist allerdings
- dass das Design selbst in der kleinen Ansicht (Suchergebnisse) auf Vendora klar hervorsticht, das heißt dort klar erkennbar und die Schrift sofort lesbar ist. Es muss in klein „wirken“, weil viele mit dem Handy auf Vendora shoppen und die Ansicht in den Suchergebnissen dort noch kleiner ist.
- dass das Design die gezielt Emotionen vermittelt
Optimal wäre es, wenn Ihr keine Mockups hochladet. Das macht es viel schwieriger, die Designs einzuschätzen und miteinander zu vergleichen.

```html
<!DOCTYPE html>
<html lang="de">
<head>
<meta charset="utf-8">
<title>Mondgarten am Nordufer – Buchcover</title>
<link rel="stylesheet" href="https://fonts.googleapis.com/css2?family=Courgette&family=Fira+Sans+Condensed:wght@500;600&display=swap">
<style>
  :root {
    --canvas: #ffffff;
    --cover-pink: #f5bccb;
    --accent-red: #e31b3c;
    --title-white: #ffffff;
    --photo-top: #c9a08f;
    --photo-bottom: #e3aab6;
  }
  * { margin: 0; padding: 0; box-sizing: border-box; }
  html, body {
    width: 1200px; height: 1200px; overflow: hidden;
    background: var(--canvas);
  }
  .stage { position: relative; width: 1200px; height: 1200px; }
  .book-cover {
    position: absolute; left: 359px; top: 255px;
    width: 482px; height: 690px;
    background: var(--cover-pink);
    overflow: hidden;
  }
  .author {
    position: absolute; top: 20px; left: 0; right: 0;
    text-align: center;
    font-family: "Fira Sans Condensed", sans-serif;
    font-weight: 600; font-size: 15px;
    color: var(--accent-red);
  }
  .title {
    position: absolute; top: 44px; left: 0; right: 0;
    text-align: center;
    font-family: "Courgette", cursive;
    font-weight: 400; font-size: 70px; line-height: 94px;
    color: var(--title-white);
    white-space: nowrap;
    text-shadow: 3px 4px 6px rgba(150, 60, 80, 0.35);
  }
  .title span { display: block; }
  .cover-photo {
    position: absolute; left: 245px; top: 245px;
    width: 195px; height: 360px;
    background: linear-gradient(180deg, var(--photo-top) 0%, var(--photo-bottom) 100%);
    opacity: 0.55;
  }
  .subtitle {
    position: absolute; left: 33px; top: 266px;
    font-family: "Fira Sans Condensed", sans-serif;
    font-weight: 600; font-size: 18px; line-height: 23px;
    color: var(--accent-red);
    white-space: nowrap;
  }
  .subtitle span { display: block; }
  .tagline-band {
    position: absolute; left: 0; bottom: 0;
    width: 100%; height: 85px;
    background: var(--accent-red);
    display: flex; flex-direction: column; justify-content: center; align-items: center;
    font-family: "Fira Sans Condensed", sans-serif;
    font-weight: 600; font-size: 21px; line-height: 31px;
    color: var(--title-white);
    text-align: center;
  }
</style>
</head>
<body>
<div class="stage">
  <div class="book-cover">
    <div class="cover-photo" role="img" aria-label="Foto einer lächelnden Frau in geblümtem Kleid, die ein großes rotes Herz umarmt"></div>
    <p class="author">Max Mustermann</p>
    <h1 class="title"><span>Mondgarten</span><span>am Nordufer</span></h1>
    <p class="subtitle">
      <span>Wie du dich von negativen</span>
      <span>Gedanken befreist und</span>
      <span>eine liebevolle Beziehung</span>
      <span>zu dir selbst aufbaust</span>
    </p>
    <div class="tagline-band">
      <span>12 lebensverändernde Monate</span>
      <span>voller positiver Impulse und Liebe für dich</span>
    </div>
  </div>
</div>
</body>
</html>
```